Business cards for a naturopathic day clinic for stem cell therapy

We need a basic design for a day clinic, that offers stem cell therapies for Lyme therapy and other severe chronic illnesses.
Our name is "Haus solvaKrĂ¤ut", which can be translated into "Manor solvaHerb". We are a couple of naturopaths working along side physiotherapists and osteopaths, yoga teachers and massage therapists. I attached our logo.

```html
<!DOCTYPE html>
<html lang="en">
<head>
<meta charset="utf-8">
<title>Clearwater Day Clinic – Business Cards</title>
<link href="https://fonts.googleapis.com/css2?family=Montserrat:wght@400;500;600&display=swap" rel="stylesheet">
<style>
  :root {
    --page-bg: #dcdcdc;
    --card-bg: #8a7362;
    --card-bg-light: #947d6c;
    --accent-green: #a6c63b;
    --text-white: #ffffff;
    --card-radius: 22px;
  }
  * { box-sizing: border-box; margin: 0; padding: 0; }
  html, body {
    width: 1200px;
    height: 800px;
    overflow: hidden;
    background: var(--page-bg);
    font-family: "Montserrat", sans-serif;
  }
  .canvas {
    width: 1200px;
    height: 800px;
    display: flex;
    align-items: center;
    justify-content: center;
    gap: 40px;
  }
  .card {
    position: relative;
    width: 540px;
    height: 309px;
    border-radius: var(--card-radius);
    background: var(--card-bg);
    overflow: hidden;
  }

  /* Contact side */
  .card-back__texture {
    position: absolute;
    inset: 0;
    background: linear-gradient(120deg, var(--card-bg-light) 0%, var(--card-bg) 55%, var(--card-bg-light) 100%);
  }
  .card-back__content {
    position: absolute;
    inset: 0;
    display: flex;
    align-items: center;
    padding: 0 36px 0 40px;
  }
  .holder {
    flex: 0 0 210px;
    text-align: right;
    padding-right: 18px;
  }
  .holder__name {
    color: var(--accent-green);
    font-weight: 600;
    font-size: 21px;
    letter-spacing: 0.04em;
    text-transform: uppercase;
    line-height: 1.1;
  }
  .holder__role {
    color: var(--text-white);
    font-weight: 600;
    font-size: 13px;
    margin-top: 2px;
  }
  .divider {
    width: 1px;
    height: 110px;
    background: var(--accent-green);
    flex: 0 0 1px;
  }
  .contact-list {
    list-style: none;
    padding-left: 18px;
    color: var(--text-white);
    font-size: 12.5px;
    line-height: 1.42;
  }
  .contact-list li {
    display: flex;
    align-items: flex-start;
    gap: 8px;
  }
  .contact-list svg {
    flex: 0 0 11px;
    width: 11px;
    height: 11px;
    margin-top: 3px;
  }
  .contact-list .icon-green { fill: var(--accent-green); }
  .contact-list .icon-white { fill: none; stroke: var(--text-white); stroke-width: 1.6; }
  .contact-gap { margin-top: 6px; }

  /* Name side */
  .card-front__content {
    position: absolute;
    inset: 0;
    display: flex;
    align-items: center;
    justify-content: center;
    gap: 16px;
    padding: 0 30px;
  }
  .brand-dot {
    flex: 0 0 46px;
    width: 46px;
    height: 46px;
    border-radius: 50%;
    background: var(--accent-green);
  }
  .brand-name {
    color: var(--accent-green);
    font-weight: 500;
    font-size: 32px;
    white-space: nowrap;
  }
</style>
</head>
<body>
<main class="canvas">

  <section class="card card-back" aria-label="Business card, contact side">
    <div class="card-back__texture" role="img" aria-label="Soft rounded background pattern in light and dark brown tones"></div>
    <div class="card-back__content">
      <div class="holder">
        <p class="holder__name">Jonas Berger</p>
        <p class="holder__role">President</p>
      </div>
      <div class="divider"></div>
      <ul class="contact-list">
        <li>
          <svg viewBox="0 0 12 12" aria-hidden="true"><path class="icon-green" d="M6 0a4 4 0 0 0-4 4c0 3 4 8 4 8s4-5 4-8a4 4 0 0 0-4-4zm0 5.6A1.6 1.6 0 1 1 6 2.4a1.6 1.6 0 0 1 0 3.2z"/></svg>
          <span>412 Linden Grove<br>Juneau, Alaska 99801</span>
        </li>
        <li class="contact-gap">
          <svg viewBox="0 0 12 12" aria-hidden="true"><path class="icon-green" d="M2.4 0.6l2 2.2-1 1.4c.7 1.6 1.9 2.8 3.5 3.5l1.4-1 2.2 2-1.2 2.2C5 10.6 1.4 7 0.2 1.8z"/></svg>
          <span>555-214-7730</span>
        </li>
        <li>
          <svg viewBox="0 0 12 12" aria-hidden="true"><rect class="icon-white" x="1.5" y="2" width="9" height="8" rx="1"/></svg>
          <span>555-318-4462</span>
        </li>
        <li>
          <svg viewBox="0 0 12 12" aria-hidden="true"><rect class="icon-white" x="3" y="0.8" width="6" height="10.4" rx="1"/></svg>
          <span>555-406-1195</span>
        </li>
        <li>
          <svg viewBox="0 0 12 12" aria-hidden="true"><path class="icon-white" d="M1 2.5h10v7H1zM1 2.5l5 4 5-4"/></svg>
          <span>info@clearwaterclinic.com</span>
        </li>
        <li>
          <svg viewBox="0 0 12 12" aria-hidden="true"><circle class="icon-green" cx="6" cy="6" r="5.5"/></svg>
          <span>clearwaterclinic.com</span>
        </li>
      </ul>
    </div>
  </section>

  <section class="card card-front" aria-label="Business card, name side">
    <div class="card-front__content">
      <span class="brand-dot" aria-hidden="true"></span>
      <h1 class="brand-name">Clearwater Day Clinic</h1>
    </div>
  </section>

</main>
</body>
</html>
```